Business Card Design

I would like a simple logo for Marwick Holdings.
We run a company that looks after our extended
family's investments.

Industry/Entity Type

Business

Contact Information for Business Card

Colleen Barfoot
Director
Marwick Holdings
ABN 72 318 506 942
Investment Management
colleen@marwickholdings.com.au
Mobile +61 437 880 642
Level 1, 57 Paxton St
Townsville, Qld 4810

```html
<!DOCTYPE html>
<html lang="en">
<head>
<meta charset="utf-8">
<title>Marwick Holdings – Business Card</title>
<link rel="stylesheet" href="https://fonts.googleapis.com/css2?family=Open+Sans:wght@600&family=Old+Standard+TT:wght@400&display=swap">
<style>
  :root {
    --backdrop: #e9e6e4;
    --card: #ffffff;
    --ink: #111111;
    --brand-red: #d01f26;
    --band: #0c0c0c;
    --band-edge: #e0262b;
  }
  * { box-sizing: border-box; margin: 0; padding: 0; }
  html, body {
    width: 1200px;
    height: 800px;
    overflow: hidden;
    background: var(--backdrop);
  }
  .card {
    position: absolute;
    left: 120px;
    top: 120px;
    width: 960px;
    height: 560px;
    background: var(--card);
    box-shadow: 0 18px 40px rgba(0,0,0,0.18);
    overflow: hidden;
  }
  .brand {
    position: absolute;
    left: 70px;
    top: 70px;
    display: flex;
    align-items: center;
    gap: 26px;
  }
  .brand-dot {
    width: 118px;
    height: 118px;
    border-radius: 50%;
    background: var(--brand-red);
    flex: none;
  }
  .brand-text { display: flex; flex-direction: column; }
  .brand-name {
    font-family: "Open Sans", sans-serif;
    font-weight: 600;
    font-size: 54px;
    line-height: 1;
    color: var(--ink);
    letter-spacing: -0.5px;
  }
  .brand-rule {
    height: 3px;
    background: var(--brand-red);
    margin: 10px 0 8px;
    width: 560px;
  }
  .brand-tagline {
    font-family: "Open Sans", sans-serif;
    font-weight: 600;
    font-size: 14px;
    letter-spacing: 11px;
    color: var(--ink);
  }
  .contact {
    position: absolute;
    left: 70px;
    top: 245px;
    font-family: "Old Standard TT", serif;
    color: var(--ink);
  }
  .person-name {
    font-size: 30px;
    color: var(--brand-red);
    line-height: 1.1;
  }
  .person-role {
    font-size: 17px;
    margin: 4px 0 14px 10px;
  }
  .contact-list { list-style: none; }
  .contact-list li {
    display: flex;
    align-items: flex-start;
    gap: 10px;
    font-size: 24px;
    line-height: 30px;
  }
  .contact-icon {
    width: 22px;
    height: 22px;
    flex: none;
    margin-top: 5px;
  }
  .contact-list .indent { padding-left: 32px; }
  .contact-list .abn {
    padding-left: 32px;
    font-size: 18px;
    line-height: 26px;
  }
  .card-band {
    position: absolute;
    left: 0;
    bottom: 0;
    width: 100%;
    height: 30px;
    background: var(--band);
    border-top: 4px solid var(--band-edge);
  }
</style>
</head>
<body>
  <div class="card">
    <div class="brand">
      <div class="brand-dot"></div>
      <div class="brand-text">
        <span class="brand-name">Marwick Holdings</span>
        <div class="brand-rule"></div>
        <span class="brand-tagline">INVESTMENT MANAGEMENT</span>
      </div>
    </div>

    <div class="contact">
      <div class="person-name">Colleen Barfoot</div>
      <div class="person-role">Director</div>
      <ul class="contact-list">
        <li>
          <svg class="contact-icon" viewBox="0 0 24 24" aria-hidden="true">
            <rect x="6" y="2" width="12" height="20" rx="2" fill="none" stroke="#d01f26" stroke-width="2.2"/>
            <rect x="8.5" y="5" width="7" height="6" fill="#d01f26"/>
            <circle cx="12" cy="18" r="1.5" fill="#d01f26"/>
          </svg>
          <span>+61 437 880 642</span>
        </li>
        <li>
          <svg class="contact-icon" viewBox="0 0 24 24" aria-hidden="true">
            <rect x="2" y="5" width="20" height="14" rx="1.5" fill="#d01f26"/>
            <path d="M3 6 L12 13 L21 6" fill="none" stroke="#fff" stroke-width="1.8"/>
          </svg>
          <span>colleen@marwickholdings.com.au</span>
        </li>
        <li>
          <svg class="contact-icon" viewBox="0 0 24 24" aria-hidden="true">
            <path d="M12 3 L2 12 H5 V21 H10 V15 H14 V21 H19 V12 H22 Z" fill="#d01f26"/>
          </svg>
          <span>Level 1, 57 Paxton St</span>
        </li>
        <li class="indent">Townsville, Qld 4810</li>
        <li class="abn">ABN 72 318 506 942</li>
      </ul>
    </div>

    <div class="card-band"></div>
  </div>
</body>
</html>
```